Optometry office needs a postcard to get name out to local schools

I need a postcard design for an optometry office called "Hosaru Optometry".
I want to get our name out to local schools and with this short letter and advertisement.
I want to keep the baby blue /navy blue colors theme.
One the front i want the following
Front:
1) three lines for the address of the recipient as in the example, and square for the postage in the upper right hand corner.
2) our logo with "Hosaru Optometry" and a horizontal line with our website address just below the line as in the example.
put the words "Our practice is committed to supporting our community and local schools." and our phone number "714-390-5264"
3) perhaps more contact info is looks neat and not too cluttered
Back:
1) letter which is attached
2) maybe a small clip art like a phoropter or glasses or something eye related

```html
<!DOCTYPE html>
<html lang="en">
<head>
<meta charset="utf-8">
<title>Hosaru Optometry – School Postcard</title>
<link href="https://fonts.googleapis.com/css2?family=Arimo:wght@400;700&display=swap" rel="stylesheet">
<style>
  :root {
    --backdrop: #222222;
    --navy: #2e3192;
    --sky: #8fb0da;
    --sky-line: #7fa3d4;
    --teal: #36b99d;
    --teal-dark: #2a9c86;
    --ink: #5a5a5a;
    --white: #ffffff;
    --photo-light: #c9d4dd;
    --photo-warm: #b9a48e;
  }
  * { margin: 0; padding: 0; box-sizing: border-box; }
  html, body { width: 1200px; height: 900px; overflow: hidden; }
  body {
    background: var(--backdrop);
    font-family: "Arimo", Arial, sans-serif;
    position: relative;
  }
  .card {
    position: absolute;
    top: 38px;
    width: 586px;
    height: 824px;
    background: var(--white);
    overflow: hidden;
  }
  .card--letter { left: 8px; }
  .card--address { left: 606px; }
  .card-bg { position: absolute; inset: 0; width: 100%; height: 100%; }
  .abs { position: absolute; }

  /* brand wordmark */
  .wordmark {
    position: absolute;
    color: var(--navy);
    font-weight: 400;
    line-height: 1;
    text-align: right;
  }
  .wordmark .brand-main { display: block; font-size: 62px; letter-spacing: 1px; }
  .wordmark .brand-sub { display: block; font-size: 25px; letter-spacing: 2px; margin-top: 6px; }
  .brand-dot {
    position: absolute;
    border-radius: 50%;
    background: var(--sky);
  }

  /* letter side */
  .doctor-name { left: 14px; top: 6px; font-size: 28px; font-weight: 700; color: var(--navy); letter-spacing: 1px; }
  .doctor-title { left: 20px; top: 44px; font-size: 16px; color: var(--navy); letter-spacing: .5px; }
  .salutation { left: 14px; top: 316px; font-size: 18px; font-weight: 700; color: var(--navy); }
  .letter-body { left: 16px; top: 345px; font-size: 13.5px; line-height: 19.2px; color: var(--ink); }
  .letter-body p { margin-bottom: 7px; }
  .letter-body .w1 { width: 560px; }
  .letter-body .w2 { width: 512px; }
  .letter-body .w3 { width: 456px; }
  .letter-body .w4 { width: 345px; }
  .sign-off { left: 22px; top: 674px; font-size: 13.5px; line-height: 20px; color: var(--ink); }
  .sign-off span { display: block; padding-left: 19px; }
  .sign-off span + span { padding-left: 0; }

  /* address side */
  .headline {
    left: 17px; top: 300px;
    font-size: 31px; line-height: 33px;
    color: var(--ink); letter-spacing: 1px;
  }
  .headline b { font-weight: 700; }
  .contact { left: 17px; top: 440px; color: var(--ink); }
  .contact .c-name { font-size: 20px; font-weight: 700; letter-spacing: .5px; }
  .contact .c-line { font-size: 19px; line-height: 24px; letter-spacing: .5px; }
  .contact .c-small { font-size: 15px; line-height: 22px; letter-spacing: .5px; padding-left: 2px; }
  .contact .c-name + .c-line { margin-top: 2px; }
  .contact .c-line + .c-small { margin-top: 6px; }
  .postage-box {
    left: 458px; top: 420px; width: 94px; height: 120px;
    border: 3px dashed var(--white);
  }
  .address-line { left: 257px; width: 298px; height: 3px; background: var(--white); }
  .web { left: 0; width: 586px; text-align: center; color: var(--white); font-weight: 700; font-size: 19px; letter-spacing: 1px; }
</style>
</head>
<body>

<!-- Letter side -->
<section class="card card--letter">
  <svg class="card-bg" viewBox="0 0 586 824" aria-hidden="true">
    <path d="M0 0 H586 V165 C480 160 390 200 310 255 C230 310 110 310 0 245 Z" fill="var(--sky)"/>
    <path d="M0 245 C110 310 230 310 310 255 C390 200 480 160 586 165" fill="none" stroke="var(--teal)" stroke-width="14"/>
    <path d="M0 265 C110 335 240 332 320 272 C400 215 480 182 586 185" fill="none" stroke="var(--sky-line)" stroke-width="5"/>
    <path d="M0 824 V760 C220 790 430 700 586 420 V824 Z" fill="var(--teal)"/>
    <path d="M0 752 C220 782 430 692 586 410" fill="none" stroke="var(--sky-line)" stroke-width="10"/>
    <circle cx="482" cy="244" r="102" fill="var(--sky-line)"/>
    <circle cx="482" cy="244" r="95" fill="var(--teal)"/>
  </svg>

  <div class="abs" role="img" aria-label="Phoropter eye-testing instrument"
       style="left:40px;top:105px;width:200px;height:195px;border-radius:24px;background:radial-gradient(circle,#8c9096 0%,#c8ccd0 70%,rgba(255,255,255,0) 100%);"></div>
  <div class="abs" role="img" aria-label="Child having an eye exam behind a phoropter"
       style="left:394px;top:156px;width:176px;height:176px;border-radius:50%;background:linear-gradient(160deg,var(--photo-light),#7d7f86 70%,#4f4a52);"></div>
  <div class="abs" role="img" aria-label="Optometrist examining a smiling patient at a slit lamp"
       style="left:240px;top:690px;width:346px;height:134px;background:linear-gradient(90deg,rgba(54,185,157,0) 0%,rgba(42,156,134,.85) 35%,var(--teal-dark) 100%);"></div>

  <div class="abs doctor-name">Daniel Hosaru, OD</div>
  <div class="abs doctor-title">OPTOMETRIST</div>

  <span class="brand-dot" style="left:330px;top:92px;width:18px;height:18px;"></span>
  <div class="wordmark" style="right:14px;top:62px;">
    <span class="brand-main">Hosaru</span>
    <span class="brand-sub">OPTOMETRY</span>
  </div>

  <div class="abs salutation">Dear</div>
  <div class="abs letter-body">
    <p class="w1">I would like to introduce our family optometry office that has been in business for the past 35 years! We are located at 4120 Maple Grove Ave Ste B in Lakemont (near Maple Grove Ave and Cedar St).</p>
    <p class="w2">Our practice is committed to supporting our community and local schools by taking care of adults and children of all ages. As 80% of learning is done visually, it is especially important for young children to have access to routine comprehensive eye care. Our goal is to provide excellent eye care for families as well as quality ophthalmic frames and lenses at reasonable prices.</p>
    <p class="w3">We are happy to see any referrals from you, including students who have not passed vision screenings or have other ocular health concerns. Please feel free to reach out to us if you have any questions. You can contact us by phone or email, and are also welcome to visit our office anytime.</p>
    <p class="w4">We look forward to a strong relationship together and success for all your students.</p>
  </div>
  <div class="abs sign-off">
    <span>Sincerely</span>
    <span>Daniel Hosaru, OD</span>
  </div>
</section>

<!-- Address side -->
<section class="card card--address">
  <svg class="card-bg" viewBox="0 0 586 824" aria-hidden="true">
    <path d="M0 0 H140 C90 8 40 22 0 48 Z" fill="#3f86c8"/>
    <path d="M586 30 C560 330 380 560 0 650 V824 H586 Z" fill="var(--teal)"/>
    <path d="M586 0 C572 300 400 540 0 648" fill="none" stroke="var(--sky-line)" stroke-width="9"/>
    <circle cx="129" cy="157" r="122" fill="var(--teal)"/>
  </svg>

  <div class="abs" role="img" aria-label="Optometrist examining a patient with a phoropter"
       style="left:15px;top:43px;width:228px;height:228px;border-radius:50%;background:linear-gradient(120deg,#dfe3e6 0%,var(--photo-warm) 55%,#e8e4df 100%);"></div>

  <span class="brand-dot" style="left:258px;top:80px;width:18px;height:18px;"></span>
  <div class="wordmark" style="right:50px;top:58px;">
    <span class="brand-main" style="font-size:68px;">Hosaru</span>
    <span class="brand-sub" style="font-size:28px;">OPTOMETRY</span>
  </div>

  <div class="abs headline">
    <b>Our practice</b> is committed to<br>
    supporting <b>our community</b><br>
    and local schools.
  </div>

  <div class="abs contact">
    <div class="c-name">Daniel Hosaru, OD</div>
    <div class="c-line">OPTOMETRIST</div>
    <div class="c-line">4120 Maple Grove Ave Ste B</div>
    <div class="c-line">Lakemont, CA 90641</div>
    <div class="c-small">Ph. 714.390.5264</div>
    <div class="c-small" style="margin-top:0;">Fax 714.390.5265</div>
  </div>

  <div class="abs postage-box"></div>
  <div class="abs address-line" style="top:590px;"></div>
  <div class="abs address-line" style="top:654px;"></div>
  <div class="abs address-line" style="top:718px;"></div>

  <div class="abs web" style="top:757px;">hello@hosaruoptometry.com</div>
  <div class="abs web" style="top:785px;">www.hosaruoptometry.com</div>
</section>

</body>
</html>
```